Women's Shelter Website Design

We are working with a Women's Shelter in California. They provide services and shelter for women and mothers throughout California.
Some sites to use for inspiration:
https://harborlightrefuge.org
https://pkrtb.org
https://www.qelmrd.org
https://brqfernhollow.org
https://www.kvsafepath.org (I love the banner, navigation and upper navigation)
https://stonebrookrest.org (love the idea of an EXIT NOW button)
Thank you for taking the time to consider designing a website for us. We are web developers based in Stockton, CA, USA. Most of our projects go through the same process. Understanding this process may help you win a project with us. We custom-code all of our websites in-house. We don’t have any requirements as to what tools you use for your design, but we ask that you follow these guidelines.
IMAGES:
If you use any images or icons in the design, we ask that you have a link to the asset so we can purchase the image/icon. Most of the designs we submit do not have the customer’s images on them unless they have some great images. Be creative; show us the feeling you are trying to portray with your image choices. Use any royalty-free site you choose. We subscribe to Quillmere and mainly use their images, but we can purchase images outside of Quillmere. PLEASE NOTE: we will not submit designs to clients with watermarks on the images.
FONTS:
We ask that you identify the fonts you’re using in the design. This can be done in a message if you want. We typically use Brightleaf Type and Quillmere Fonts.
CONTENT:
We're always open to different content and ideas. We often submit designs with stock images so the client can see our vision. We typically take pictures after the website launch to use their images with our vision. Lorem Ipsum is fine for paragraphs, but we ask that you make the Headers with correct English. We want to be able to show the vision and identify the sections of the website.
INSPIRATION:
We typically add a couple of links in the brief of websites we like to help you get started in your design.
REVISIONS:
We do not often ask for revisions of the designs unless we see something in the design that may not appeal to the client. If there are slight changes that we want to make, we do that in the development process.
FEEDBACK:
We rarely give feedback on designs during the design process. We are working on many website projects and do not have the time to provide feedback. We usually respond if your request is well thought out and asks specific questions, but a note asking “feedback, please” usually goes unanswered.

```html
<!DOCTYPE html>
<html lang="en">
<head>
<meta charset="utf-8">
<title>Wingrest Women's Shelter</title>
<link rel="stylesheet" href="https://fonts.googleapis.com/css2?family=Montserrat:wght@400;500;600;700;800&family=Poppins:wght@400;500;600;700&display=swap">
<style>
:root{
  --purple:#3d1a78;
  --purple-dark:#2c1060;
  --coral:#f25c4a;
  --green:#2fa84f;
  --grey-bg:#f3f3f3;
  --text:#6f6f6f;
  --heading-grey:#7a7a7a;
  --white:#ffffff;
}
*{box-sizing:border-box;margin:0;padding:0}
html,body{width:1200px;height:5029px;overflow:hidden}
body{font-family:"Montserrat",sans-serif;color:var(--text);background:var(--white);position:relative}
.section{position:absolute;left:0;width:1200px;overflow:hidden}
.abs{position:absolute}
.eyebrow{position:absolute;font-size:17px;letter-spacing:1px;color:#555;font-weight:500}
.eyebrow .dots{color:var(--coral);letter-spacing:3px;font-weight:700}
.title{position:absolute;font-family:"Poppins",sans-serif;font-weight:600;color:var(--purple);letter-spacing:.5px}
.center{left:0;width:1200px;text-align:center}
.pill{position:absolute;display:flex;align-items:center;justify-content:space-between;border-radius:22px;font-size:13px;font-weight:500;padding:0 5px 0 16px}
.pill .arrow{width:30px;height:30px;border-radius:50%;background:var(--coral);display:flex;align-items:center;justify-content:center}
.pill-solid{background:var(--purple);color:var(--white)}
.pill-outline{border:2px solid #f6a89e;color:#555;background:var(--white)}
.photo{position:absolute}

/* top bar */
.topbar{top:0;height:68px;background:#efefef}
.brand{position:absolute;left:52px;top:22px;display:flex;align-items:center;gap:8px;font-family:"Poppins",sans-serif;font-weight:700;font-size:19px;color:#1d1d1d}
.brand .mark{width:20px;height:20px;border-radius:50%;background:var(--purple)}
.quick-actions{position:absolute;top:20px;left:752px;display:flex}
.quick-actions span{display:block;height:30px;line-height:30px;color:var(--white);font-size:12px;font-weight:600;text-align:center;clip-path:polygon(14px 0,100% 0,calc(100% - 14px) 100%,0 100%);margin-right:-10px}
.qa-help{background:var(--purple);width:140px}
.qa-vol{background:var(--coral);width:140px}
.qa-donate{background:var(--green);width:140px}
.mainnav{top:68px;height:50px;background:var(--white)}
.mainnav ul{list-style:none;position:absolute;top:0;left:0;width:100%;height:50px}
.mainnav li{position:absolute;top:16px;font-size:13px;font-weight:500;color:#222}
.search{position:absolute;left:996px;top:11px;width:30px;height:30px;border:1.5px solid var(--purple);border-radius:50%}

/* hero */
.hero{top:118px;height:604px;background:linear-gradient(90deg,#f6f5f4 0%,#f2efec 50%,#ece7e2 100%)}
.hero-photo{left:560px;top:0;width:640px;height:604px;background:
  radial-gradient(ellipse 160px 220px at 78% 45%,#3a2a24 0%,rgba(58,42,36,0) 100%),
  radial-gradient(ellipse 140px 110px at 45% 22%,#f3d6c8 0%,rgba(243,214,200,0) 100%),
  linear-gradient(90deg,rgba(240,236,232,0) 0%,#ebe3dc 30%,#d8c8bb 70%,#cbbcb0 100%)}
.hero h1{position:absolute;left:50px;top:140px;font-family:"Poppins",sans-serif;font-size:66px;font-weight:700;color:var(--purple);letter-spacing:-.5px}
.hero p{position:absolute;left:50px;top:258px;width:450px;font-size:16px;line-height:21px;color:#555}
.btn-learn{position:absolute;left:50px;top:409px;width:146px;height:36px;background:var(--purple);color:var(--white);font-size:13px;font-weight:500;display:flex;align-items:center;justify-content:center;gap:8px;border-radius:3px}

/* about */
.about{top:722px;height:640px;background:var(--grey-bg)}
.about p{position:absolute;left:128px;width:462px;font-size:14.5px;line-height:18px;color:#666}

/* what we do */
.whatwedo{top:1362px;height:482px;background:var(--white)}
.wd-heading{position:absolute;font-size:26px;font-weight:500;color:var(--heading-grey);white-space:nowrap}
.wd-heading.right{text-align:right;width:200px}
.wd-center{position:absolute;left:480px;top:388px;width:280px;text-align:center;font-family:"Poppins",sans-serif;font-weight:700;font-size:44px;color:#222}
.wd-sub{position:absolute;left:480px;top:452px;width:280px;text-align:center;font-size:10px;letter-spacing:4px;color:#aaa}

/* services */
.services{top:1844px;height:747px;background:var(--grey-bg)}
.card{position:absolute;top:185px;width:318px;height:445px;background:var(--white);box-shadow:0 4px 16px rgba(0,0,0,.08)}
.card .photo{left:25px;top:25px;width:266px;height:200px}
.card h3{position:absolute;left:25px;top:243px;font-family:"Poppins",sans-serif;font-size:18px;font-weight:600;color:var(--purple)}
.card p{position:absolute;left:25px;top:284px;width:272px;font-size:12.5px;line-height:24px;color:#888}
.card .pill{left:25px;top:370px;width:146px;height:40px}
.dot{position:absolute;top:703px;width:18px;height:18px;border-radius:50%;background:var(--coral)}
.dot.empty{background:transparent;border:2px solid var(--coral)}

/* involved */
.involved{top:2591px;height:618px}
.involved-bg{left:0;top:0;width:1200px;height:618px;background:
  radial-gradient(ellipse 380px 200px at 55% 55%,#6e5c50 0%,rgba(110,92,80,0) 100%),
  radial-gradient(ellipse at 55% 45%,#4e4a47 0%,#353230 45%,#232120 100%)}
.involved h2{position:absolute;top:185px;font-family:"Poppins",sans-serif;font-size:28px;font-weight:600;color:var(--white);letter-spacing:.5px}
.involved p{position:absolute;left:240px;top:270px;width:720px;text-align:center;font-size:15px;line-height:31px;color:var(--white);letter-spacing:1px;font-weight:500}
.involved .pill{left:484px;top:403px;width:180px;height:44px;border:3px solid var(--white);font-weight:600}

/* blogs */
.blogs{top:3209px;height:810px;background:var(--white)}
.blog-intro{position:absolute;top:186px;font-size:15px;color:#444}
.blog{position:absolute;top:253px;width:309px;height:538px;border:1px solid #dcdcdc;background:var(--white)}
.blog .photo{left:0;top:0;width:307px;height:300px}
.blog .date{position:absolute;left:26px;top:327px;font-size:12px;color:var(--coral)}
.blog h3{position:absolute;left:26px;top:362px;font-family:"Poppins",sans-serif;font-size:22px;font-weight:600;color:var(--purple)}
.blog p{position:absolute;left:26px;top:406px;width:250px;font-size:13px;line-height:17px;color:#555}
.blog .pill{left:20px;top:488px;width:146px;height:40px}

/* contact */
.contact{top:4019px;height:658px;background:var(--white)}
.field{position:absolute;left:593px;width:567px;background:#ededed;border:1px solid #cfcfcf;font-size:15px;color:#aaa;padding:16px 22px}

/* footer */
.footer{top:4677px;height:352px;background:linear-gradient(180deg,#4a1f86 0%,#8b3273 45%,#e3534f 100%);color:var(--white)}
.footer h4{position:absolute;top:66px;font-size:17px;font-weight:600;letter-spacing:.5px}
.footer-links{position:absolute;top:104px;left:0;width:1200px;display:flex;justify-content:center;gap:12px;font-size:13px;font-weight:500}
.signup{position:absolute;top:152px;font-size:14px;font-weight:500}
.news-input{position:absolute;left:375px;top:190px;width:335px;height:38px;background:var(--white);color:#999;font-size:13px;padding:11px 10px}
.news-btn{position:absolute;left:710px;top:190px;width:115px;height:38px;background:var(--purple-dark);font-size:12px;font-weight:700;display:flex;align-items:center;justify-content:center;border:1px solid var(--white)}
.social{position:absolute;top:253px;width:19px;height:19px;border-radius:50%;background:var(--white)}
.footer hr{position:absolute;left:25px;top:300px;width:1150px;border:0;border-top:1px solid rgba(255,255,255,.6)}
.copy{position:absolute;top:313px;font-size:14px}
</style>
</head>
<body>

<header class="section topbar">
  <div class="brand"><span class="mark"></span>Wingrest</div>
  <div class="quick-actions">
    <span class="qa-help">GET HELP NOW</span>
    <span class="qa-vol">VOLUNTEER</span>
    <span class="qa-donate">DONATE</span>
  </div>
</header>

<nav class="section mainnav">
  <ul>
    <li style="left:195px">HOME ›</li>
    <li style="left:303px">ABOUT ›</li>
    <li style="left:415px">WHAT WE DO ›</li>
    <li style="left:568px">GET INVOLVED ›</li>
    <li style="left:733px">CAPITAL CAMPAIGN ›</li>
    <li style="left:942px">BLOG</li>
  </ul>
  <div class="search">
    <svg width="27" height="27" viewBox="0 0 27 27"><circle cx="12.5" cy="12.5" r="4" fill="none" stroke="#3d1a78" stroke-width="1.8"/><line x1="15.5" y1="15.5" x2="18.5" y2="18.5" stroke="#3d1a78" stroke-width="1.8"/></svg>
  </div>
</nav>

<section class="section hero">
  <div class="photo hero-photo" role="img" aria-label="Mother lifting her baby up in a bright room"></div>
  <h1>Safe Haven</h1>
  <p>Lorem ipsum dolor sit amet, consectetur adipiscing elit, sed do eiusmod tempor incididunt ut labore et dolore magna aliqua. Quis ipsum suspendisse ultrices gravida. Risus commodo viverra maecenas</p>
  <div class="btn-learn">LEARN MORE <svg width="12" height="10" viewBox="0 0 12 10"><path d="M0 5h10M6 1l4 4-4 4" fill="none" stroke="#fff" stroke-width="1.5"/></svg></div>
</section>

<section class="section about">
  <div class="eyebrow" style="left:130px;top:142px"><span class="dots">•••</span> ABOUT <span class="dots">•••</span></div>
  <div class="title" style="left:128px;top:162px;font-size:32px">COMPANY</div>
  <p style="top:238px">Lorem ipsum dolor sit amet, consectetur adipiscing elit, sed do eiusmod tempor incididunt ut labore et dolore magna aliqua. Quis ipsum suspendisse ultrices gravida. Risus commodo viverra maecenas accumsan lacus vel facilisis.</p>
  <p style="top:328px">Lorem ipsum dolor sit amet, consectetur adipiscing elit, sed do eiusmod tempor incididunt ut labore et dolore magna aliqua. Quis ipsum suspendisse ultrices gravida. Risus commodo viverra maecenas accumsan lacus vel facilisis.</p>
  <div class="pill pill-solid" style="left:120px;top:446px;width:146px;height:42px">READ MORE <span class="arrow"><svg width="12" height="10" viewBox="0 0 12 10"><path d="M0 5h10M6 1l4 4-4 4" fill="none" stroke="#fff" stroke-width="1.6"/></svg></span></div>
  <svg class="abs" style="left:670px;top:65px" width="460" height="460" viewBox="0 0 460 460">
    <defs><linearGradient id="ring" x1="0" y1="1" x2="1" y2="0"><stop offset="0" stop-color="#3d1a78"/><stop offset="1" stop-color="#f8624a"/></linearGradient></defs>
    <circle cx="230" cy="225" r="222" fill="url(#ring)"/>
  </svg>
  <div class="photo" role="img" aria-label="Mother holding her children outdoors under a cloudy sky" style="left:688px;top:117px;width:390px;height:390px;border-radius:50%;background:radial-gradient(ellipse 120px 150px at 52% 72%,#6f5a52 0%,rgba(111,90,82,0) 100%),linear-gradient(180deg,#b9c2c9 0%,#ddd3c6 45%,#c9b49a 100%);box-shadow:0 6px 18px rgba(0,0,0,.2)"></div>
</section>

<section class="section whatwedo">
  <div class="eyebrow" style="left:527px;top:60px"><span class="dots">•••</span> WHAT <span class="dots">•••</span></div>
  <div class="title" style="left:534px;top:82px;font-size:38px">WE DO</div>
  <svg class="abs" style="left:0;top:0" width="1200" height="482" viewBox="0 0 1200 482">
    <defs>
      <g id="meet" fill="none" stroke="#666" stroke-width="2">
        <circle cx="-12" cy="-14" r="6"/><circle cx="12" cy="-14" r="6"/>
        <path d="M-24 14v-10a8 8 0 0 1 12-6M24 14v-10a8 8 0 0 0-12-6"/>
        <rect x="-14" y="0" width="28" height="6"/>
        <path d="M-8 6v14M8 6v14"/>
      </g>
    </defs>
    <path d="M384 388 Q420 300 503 248 Q611 180 720 248 Q803 300 837 388" fill="none" stroke="#777" stroke-width="2"/>
    <g fill="#fff" stroke="#4a2a82" stroke-width="2">
      <circle cx="384" cy="388" r="54"/><circle cx="503" cy="248" r="54"/>
      <circle cx="720" cy="248" r="54"/><circle cx="837" cy="388" r="54"/>
    </g>
    <use href="#meet" x="384" y="388"/><use href="#meet" x="503" y="248"/>
    <use href="#meet" x="720" y="248"/><use href="#meet" x="837" y="388"/>
  </svg>
  <div class="wd-heading right" style="left:124px;top:372px">Shelter</div>
  <div class="wd-heading right" style="left:241px;top:212px">Counseling</div>
  <div class="wd-heading" style="left:783px;top:212px">Legal Aid</div>
  <div class="wd-heading" style="left:903px;top:372px">Child Care</div>
  <div class="wd-center">Wingrest</div>
  <div class="wd-sub">WOMENS SHELTER</div>
</section>

<section class="section services">
  <div class="eyebrow" style="left:502px;top:66px"><span class="dots">•••</span> OUR SERVICE <span class="dots">•••</span></div>
  <div class="title center" style="top:94px;font-size:30px">OUR BEST SERVICES</div>

  <article class="card" style="left:94px">
    <div class="photo" role="img" aria-label="Counselor sitting on the floor with a mother and child" style="background:linear-gradient(180deg,#e8dccf 0%,#d9c7b4 45%,#b8453a 75%,#8a2f2a 100%)"></div>
    <h3>Service 1</h3>
    <p>Lorem ipsum dolor sit amet conse cte tur adipiscing elit sed do eiusmod tem por ares incididunt utlabore.</p>
    <div class="pill pill-outline">READ MORE <span class="arrow"><svg width="12" height="10" viewBox="0 0 12 10"><path d="M0 5h10M6 1l4 4-4 4" fill="none" stroke="#fff" stroke-width="1.6"/></svg></span></div>
  </article>

  <article class="card" style="left:437px">
    <div class="photo" role="img" aria-label="Woman and young boy looking at a tablet" style="background:linear-gradient(135deg,#f3ece2 0%,#ecd2b4 40%,#e98b4a 65%,#a9cde2 100%)"></div>
    <h3>Service 2</h3>
    <p>Lorem ipsum dolor sit amet conse cte tur adipiscing elit sed do eiusmod tem por ares incididunt utlabore.</p>
    <div class="pill pill-solid">READ MORE <span class="arrow"><svg width="12" height="10" viewBox="0 0 12 10"><path d="M0 5h10M6 1l4 4-4 4" fill="none" stroke="#fff" stroke-width="1.6"/></svg></span></div>
  </article>

  <article class="card" style="left:787px">
    <div class="photo" role="img" aria-label="Therapist taking notes while a child plays with blocks" style="background:linear-gradient(135deg,#f2f4f5 0%,#cfdae3 50%,#e7c7a2 80%,#d9a25a 100%)"></div>
    <h3>Service 3</h3>
    <p>Lorem ipsum dolor sit amet conse cte tur adipiscing elit sed do eiusmod tem por ares incididunt utlabore.</p>
    <div class="pill pill-outline">READ MORE <span class="arrow"><svg width="12" height="10" viewBox="0 0 12 10"><path d="M0 5h10M6 1l4 4-4 4" fill="none" stroke="#fff" stroke-width="1.6"/></svg></span></div>
  </article>

  <span class="dot" style="left:532px"></span>
  <span class="dot" style="left:567px"></span>
  <span class="dot empty" style="left:603px"></span>
</section>

<section class="section involved">
  <div class="photo involved-bg" role="img" aria-label="Close-up of hands holding each other in support"></div>
  <h2 class="center">GET INVOLVED WITH US</h2>
  <p>Lorem ipsum dolor sit amet, consectetur adipiscing elit, sed do eiusmod tempor incididunt ut labore et dolore magna aliqua. Quis ipsum suspendisse ultrices gravida. Risus commodo viverra maecenas accumsan lacus vel facilisis.</p>
  <div class="pill pill-solid">DONATE NOW <span class="arrow"><svg width="12" height="10" viewBox="0 0 12 10"><path d="M0 5h10M6 1l4 4-4 4" fill="none" stroke="#fff" stroke-width="1.6"/></svg></span></div>
</section>

<section class="section blogs">
  <div class="eyebrow" style="left:500px;top:96px"><span class="dots">•••</span> BLOGS <span class="dots">•••</span></div>
  <div class="title center" style="top:124px;font-size:30px">RECENT BLOGS</div>
  <div class="blog-intro center">Lorem Ipsum available, but the majority have&nbsp; suffered alteration in some form.</div>

  <article class="blog" style="left:86px">
    <div class="photo" role="img" aria-label="Mother and daughter smiling together on a yellow sofa" style="background:linear-gradient(180deg,#ece8de 0%,#e3d6c4 35%,#e8c93f 65%,#5f7aa3 100%)"></div>
    <div class="date">FEBRUARY 09, 2020</div>
    <h3>Finding Hope</h3>
    <p>Lorem Ipsum available, but the majo rity have suffered alteration in some words which look.</p>
    <div class="pill pill-outline">READ MORE <span class="arrow"><svg width="12" height="10" viewBox="0 0 12 10"><path d="M0 5h10M6 1l4 4-4 4" fill="none" stroke="#fff" stroke-width="1.6"/></svg></span></div>
  </article>

  <article class="blog" style="left:444px">
    <div class="photo" role="img" aria-label="Two women and a young boy laughing on a couch" style="background:linear-gradient(180deg,#e2ddd6 0%,#c7b8a8 40%,#7fb08d 65%,#4d6d92 100%)"></div>
    <div class="date">FEBRUARY 09, 2020</div>
    <h3>Family Support</h3>
    <p>Lorem Ipsum available, but the majo rity have suffered alteration in some words which look.</p>
    <div class="pill pill-outline">READ MORE <span class="arrow"><svg width="12" height="10" viewBox="0 0 12 10"><path d="M0 5h10M6 1l4 4-4 4" fill="none" stroke="#fff" stroke-width="1.6"/></svg></span></div>
  </article>

  <article class="blog" style="left:795px">
    <div class="photo" role="img" aria-label="Smiling woman playing with a toddler and colorful toys" style="background:linear-gradient(180deg,#dde3dc 0%,#c9a58a 35%,#6fb8b3 60%,#c7403e 100%)"></div>
    <div class="date">FEBRUARY 09, 2020</div>
    <h3>New Beginnings</h3>
    <p>Lorem Ipsum available, but the majo rity have suffered alteration in some words which look.</p>
    <div class="pill pill-outline">READ MORE <span class="arrow"><svg width="12" height="10" viewBox="0 0 12 10"><path d="M0 5h10M6 1l4 4-4 4" fill="none" stroke="#fff" stroke-width="1.6"/></svg></span></div>
  </article>
</section>

<section class="section contact">
  <div class="eyebrow" style="left:483px;top:84px"><span class="dots">•••</span> CONTACT US <span class="dots">•••</span></div>
  <div class="title center" style="top:112px;font-size:30px">GET IN TOUCH</div>
  <div class="photo" role="img" aria-label="Counselor taking notes during a conversation" style="left:40px;top:209px;width:518px;height:365px;background:radial-gradient(ellipse 180px 110px at 30% 60%,#c8b4a0 0%,rgba(200,180,160,0) 100%),linear-gradient(120deg,#3a3733 0%,#5e554d 45%,#8a7b6c 75%,#3e3a36 100%)"></div>
  <div class="field" style="top:221px;height:50px">Your Name</div>
  <div class="field" style="top:302px;height:50px">Gender</div>
  <div class="field" style="top:386px;height:121px">Messages</div>
  <div class="pill pill-solid" style="left:598px;top:533px;width:145px;height:40px">SUBMIT <span class="arrow"><svg width="12" height="10" viewBox="0 0 12 10"><path d="M0 5h10M6 1l4 4-4 4" fill="none" stroke="#fff" stroke-width="1.6"/></svg></span></div>
</section>

<footer class="section footer">
  <h4 class="center">QUICK LINK</h4>
  <div class="footer-links">
    <span>HOME</span><span>|</span><span>ABOUT</span><span>|</span><span>WHAT WE DO</span><span>|</span><span>GET INVOLVED</span><span>|</span><span>CAPITAL CAMPAIGN</span><span>|</span><span>BLOG</span>
  </div>
  <div class="signup center">Sign Up To Receive Our Newsletter</div>
  <div class="news-input">Email Here</div>
  <div class="news-btn">SUBSCRIBE</div>
  <span class="social" style="left:549px"></span>
  <span class="social" style="left:574px"></span>
  <span class="social" style="left:600px"></span>
  <span class="social" style="left:626px"></span>
  <hr>
  <div class="copy center">Copyright © 22023 . All rights reserved</div>
</footer>

</body>
</html>
```